Event Website Design

We need a new website design for an events driven website. The domain for this site is http://brackenmoorhalls.co.uk. The site is up and running but needs a new fresh, modern look.
I've attached a Balamiq Mockup for the layout of the home page. Also attached is a png of the logo.
Key colours for the site are 0f7e6a, 35bde, d57835 & 373737.
Font to use is Proxima Nova
Width of the site should be 1200px
The design should be contemporary with minimal clutter.
Websites to references are…
http://vantorium.london/
http://www.thegpz.co.uk/
These are just guidelines, please feel free to use you own creative judgment.
The selected design file needs to be supplied as an editable PSD.
Reason: I've submitted 5 designs to the client, who will select the one they want. I will then choose that design. So please be patient as I'm waiting for a decision from my client.
Events
1 page

```html
<!DOCTYPE html>
<html lang="en">
<head>
<meta charset="utf-8">
<title>Brackenmoor Halls – Entertainment &amp; Sporting Centre</title>
<link rel="stylesheet" href="https://fonts.googleapis.com/css2?family=Figtree:wght@400;500;600;700&display=swap">
<style>
:root{
  --green:#0f7e6a;
  --blue:#035bde;
  --orange:#d57835;
  --dark:#373737;
  --footer:#3b3b3b;
  --card-bg:#f4f4f4;
  --white:#ffffff;
}
*{box-sizing:border-box;margin:0;padding:0}
html,body{width:1200px;height:3072px;overflow:hidden}
body{position:relative;background:var(--white);font-family:"Figtree",Arial,sans-serif;color:var(--dark)}
.abs{position:absolute}
a{color:inherit;text-decoration:none}

/* header */
.site-header{left:0;top:0;width:1200px;height:123px}
.brand{left:70px;top:28px;width:150px;text-align:center;font-weight:700;font-size:19px;line-height:23px;letter-spacing:1px;color:var(--dark)}
.brand-divider{left:243px;top:24px;width:1px;height:70px;background:#d8d8d8}
.tagline{left:262px;top:26px;font-size:17px;line-height:21px;color:#7a7a7a}
.tagline strong{color:var(--green);font-weight:600}
.util-links{right:74px;top:16px;font-size:11px;color:#666}
.util-links span{margin:0 6px}
.box-office{left:667px;top:65px;font-size:17px;color:#777}
.box-office b{color:var(--orange);font-weight:700}
.search{left:921px;top:61px;width:205px;height:31px;border:1px solid #ddd;border-radius:16px;font-size:11px;color:#999;padding:8px 0 0 34px}
.search svg{position:absolute;left:13px;top:9px}

/* nav */
.main-nav{left:0;top:123px;width:1200px;height:49px;background:var(--dark)}
.main-nav ul{list-style:none;display:flex;position:absolute;left:74px;top:16px;gap:30px;font-size:13px;font-weight:500;color:var(--white)}
.social{top:10px;width:29px;height:29px;border:2px solid var(--white);border-radius:50%;display:flex;align-items:center;justify-content:center}

/* hero */
.hero{left:0;top:172px;width:1200px;height:555px;
  background:
    radial-gradient(circle at 8% 12%,rgba(255,196,110,.55) 0,rgba(255,196,110,0) 9%),
    radial-gradient(circle at 44% 8%,rgba(255,210,140,.5) 0,rgba(255,210,140,0) 8%),
    radial-gradient(circle at 60% 20%,rgba(255,230,180,.45) 0,rgba(255,230,180,0) 10%),
    radial-gradient(ellipse at 25% 45%,#b77a4e 0,rgba(183,122,78,0) 28%),
    radial-gradient(ellipse at 80% 40%,#a0704f 0,rgba(160,112,79,0) 30%),
    radial-gradient(ellipse at 55% 80%,#d9c7a8 0,rgba(217,199,168,0) 22%),
    linear-gradient(110deg,#2a1d14 0%,#5a3c24 40%,#2a2019 65%,#4a3526 100%)}
.hero-shade{left:0;top:440px;width:1200px;height:287px;background:linear-gradient(to bottom,rgba(0,0,0,0),rgba(0,0,0,.5))}
.date-badge{background:var(--green);color:var(--white);font-size:11px;padding:3px 7px}
.hero-date{left:74px;top:564px}
.hero-title{left:74px;top:587px;font-size:24px;font-weight:700;color:var(--white)}
.hero-text{left:74px;top:630px;width:420px;font-size:12.5px;line-height:19px;color:var(--white)}
.btn{display:flex;align-items:center;justify-content:center;font-size:12px;font-weight:500;color:var(--white)}
.btn-green{background:var(--green)}
.btn-orange{background:var(--orange)}
.hero-progress{left:285px;top:727px;width:299px;height:8px;background:var(--orange)}

/* event carousel */
.arrow{top:1037px;width:24px;height:24px;border:1.5px solid #555;border-radius:50%}
.arrow svg{position:absolute;left:6px;top:6px}
.event-card{top:793px;width:332px;height:514px;background:var(--card-bg)}
.event-card .photo{position:absolute;left:0;top:0;width:332px;height:331px}
.event-card .date{position:absolute;top:357px;width:100%;text-align:center;font-size:11px;color:#666}
.event-card h3{position:absolute;top:377px;width:100%;text-align:center;font-size:16px;font-weight:400;line-height:21px;color:var(--dark)}
.event-card .btn{position:absolute;top:444px;width:116px;height:41px}

/* news */
.news{left:0;top:1364px;width:1200px;height:541px;
  background:
    radial-gradient(ellipse at 12% 20%,rgba(40,42,46,.75) 0,rgba(40,42,46,0) 30%),
    radial-gradient(ellipse at 90% 25%,rgba(40,42,46,.7) 0,rgba(40,42,46,0) 28%),
    radial-gradient(ellipse at 30% 92%,rgba(220,222,225,.8) 0,rgba(220,222,225,0) 25%),
    radial-gradient(ellipse at 75% 90%,rgba(70,72,76,.7) 0,rgba(70,72,76,0) 26%),
    linear-gradient(100deg,#5d6166 0%,#a4a8ad 40%,#858990 70%,#4e5257 100%)}
.news-title{left:0;top:1410px;width:1200px;text-align:center;font-size:22px;font-weight:500;color:var(--white)}
.news-card{top:1489px;width:332px;height:264px;background:var(--white);padding:27px 28px}
.news-card .fold{position:absolute;right:0;top:0}
.news-card h4{font-size:15.5px;font-weight:500;line-height:20px;color:var(--dark);width:250px}
.news-card p{margin-top:17px;width:276px;font-size:12px;line-height:22px;color:#666}
.btn-outline{position:absolute;left:28px;top:192px;width:116px;height:39px;border:2px solid var(--orange);color:var(--orange);display:flex;align-items:center;justify-content:center;font-size:12px}
.see-all{left:514px;top:1810px;width:172px;height:38px;border:2px solid var(--white);color:var(--white);font-size:12px;display:flex;align-items:center;justify-content:center}

/* feature tiles */
.tile{top:1960px;width:332px;height:356px}
.tile .photo{position:absolute;left:0;top:0;width:332px;height:240px}
.tile .band{position:absolute;left:0;top:240px;width:332px;height:116px}
.tile .badge{position:absolute;left:134px;top:196px;width:64px;height:64px;border-radius:10px 10px 0 0;display:flex;align-items:center;justify-content:center}
.tile h3{position:absolute;left:0;top:270px;width:100%;text-align:center;font-size:17px;font-weight:500;color:var(--white)}
.tile .btn-line{position:absolute;left:122px;top:297px;width:88px;height:29px;border:2px solid var(--white);color:var(--white);font-size:12px;display:flex;align-items:center;justify-content:center}
.tile-blue .band,.tile-blue .badge{background:var(--blue)}
.tile-green .band,.tile-green .badge{background:var(--green)}
.tile-orange .band,.tile-orange .badge{background:var(--orange)}

/* sports */
.sports{left:0;top:2372px;width:1200px;height:462px;
  background:
    radial-gradient(ellipse at 63% 55%,#2f7fd0 0,rgba(47,127,208,0) 22%),
    radial-gradient(ellipse at 33% 55%,#c4523c 0,rgba(196,82,60,0) 14%),
    radial-gradient(ellipse at 45% 75%,#6f8aa6 0,rgba(111,138,166,0) 16%),
    radial-gradient(ellipse at 92% 45%,#e0b9a4 0,rgba(224,185,164,0) 20%),
    radial-gradient(ellipse at 72% 20%,#3a2a22 0,rgba(58,42,34,0) 15%),
    linear-gradient(100deg,#e7ddd2 0%,#bfa58f 30%,#8d7565 55%,#6a6c74 75%,#d8c3b5 100%)}
.sports-title{left:0;top:2555px;width:1200px;text-align:center;font-size:44px;font-weight:500;color:var(--white)}
.sports-sub{left:0;top:2617px;width:1200px;text-align:center;font-size:12px;color:var(--white)}

/* footer */
.site-footer{left:0;top:2834px;width:1200px;height:238px;background:var(--footer)}
.footer-col{top:2873px;font-size:12.5px;line-height:22.5px;color:#ddd}
.footer-brand{left:905px;top:2922px;width:231px;text-align:center;font-size:28px;line-height:32px;font-weight:700;letter-spacing:1px;color:var(--white)}
.copyright{left:0;top:3022px;width:1200px;text-align:center;font-size:12px;color:#bbb}
</style>
</head>
<body>

<header class="abs site-header">
  <div class="abs brand">BRACKENMOOR<br>HALLS</div>
  <div class="abs brand-divider"></div>
  <div class="abs tagline">Dunmere's Premier<br><strong>Entertainment &amp; Sporting</strong><br>Center</div>
  <div class="abs util-links">Gift Voucher<span>|</span>Join Our Mailing List<span>|</span>My Account<span>|</span>Basket<span>|</span>Register</div>
  <div class="abs box-office">Box Office : <b>01632 960 482</b></div>
  <div class="abs search">
    <svg width="12" height="12" viewBox="0 0 12 12"><circle cx="5" cy="5" r="4" fill="none" stroke="#888" stroke-width="1.5"/><line x1="8" y1="8" x2="11" y2="11" stroke="#888" stroke-width="1.5"/></svg>
    Search
  </div>
</header>

<nav class="abs main-nav">
  <ul>
    <li>What's On</li><li>Conferencing &amp; Events</li><li>Sports &amp; Leisure</li><li>Lantern Theatre</li><li>Plan Your Visit</li><li>News</li><li>Discover More</li><li>Contact</li>
  </ul>
  <a class="abs social" style="left:1024px" aria-label="Email us"><svg width="13" height="13" viewBox="0 0 14 14" fill="none" stroke="#fff" stroke-width="1.5"><rect x="1.5" y="3" width="11" height="8" rx="1"/><path d="M2 3.5 7 8l5-4.5"/></svg></a>
  <a class="abs social" style="left:1057px" aria-label="Chat with us"><svg width="13" height="13" viewBox="0 0 14 14" fill="none" stroke="#fff" stroke-width="1.5"><path d="M2 2.5h10v7H6l-3 2.5v-2.5H2z"/></svg></a>
  <a class="abs social" style="left:1090px" aria-label="Share"><svg width="13" height="13" viewBox="0 0 14 14" fill="#fff" stroke="#fff" stroke-width="1.2"><circle cx="10.5" cy="3" r="1.7"/><circle cx="3.5" cy="7" r="1.7"/><circle cx="10.5" cy="11" r="1.7"/><path d="M10.5 3 3.5 7l7 4" fill="none"/></svg></a>
</nav>

<section class="abs hero" role="img" aria-label="Friends raising champagne glasses at a candlelit dinner table"></section>
<div class="abs hero-shade"></div>
<div class="abs date-badge hero-date">Mon 7 Jan 2017</div>
<h1 class="abs hero-title">Awesome consectetur adipiscing elit</h1>
<p class="abs hero-text">Lorem ipsum dolor sit amet, consectetur adipiscing elit, sed do eiusmod tempor incididunt ut labore et dolore magna aliqua.</p>
<a class="abs btn btn-green" style="left:885px;top:629px;width:116px;height:41px">MORE</a>
<a class="abs btn btn-orange" style="left:1010px;top:629px;width:116px;height:41px">BOOK</a>
<div class="abs hero-progress"></div>

<div class="abs arrow" style="left:37px"><svg width="10" height="10" viewBox="0 0 10 10"><path d="M6.5 1.5 3 5l3.5 3.5" fill="none" stroke="#555" stroke-width="1.5"/></svg></div>
<div class="abs arrow" style="left:1139px"><svg width="10" height="10" viewBox="0 0 10 10"><path d="M3.5 1.5 7 5 3.5 8.5" fill="none" stroke="#555" stroke-width="1.5"/></svg></div>

<article class="abs event-card" style="left:74px">
  <div class="photo" role="img" aria-label="Guests mingling at a networking event" style="background:radial-gradient(ellipse at 30% 30%,#d9d3cc 0,rgba(217,211,204,0) 25%),radial-gradient(ellipse at 75% 60%,#9a4a3a 0,rgba(154,74,58,0) 20%),radial-gradient(ellipse at 40% 80%,#2d3948 0,rgba(45,57,72,0) 30%),linear-gradient(135deg,#5f6e7c,#a7a29a,#3f4853)"></div>
  <div class="date">Mon 7 Jan 2017</div>
  <h3>Awesome consectetur adipiscing<br>Guidelines elit</h3>
  <a class="btn btn-green" style="left:45px">MORE</a><a class="btn btn-orange" style="left:172px">BOOK</a>
</article>
<article class="abs event-card" style="left:434px">
  <div class="photo" role="img" aria-label="Smiling friends toasting with drinks outdoors" style="background:radial-gradient(ellipse at 60% 15%,#f2f2f0 0,rgba(242,242,240,0) 35%),radial-gradient(ellipse at 20% 50%,#3c3c3e 0,rgba(60,60,62,0) 25%),radial-gradient(ellipse at 80% 70%,#5a4a44 0,rgba(90,74,68,0) 25%),linear-gradient(135deg,#d4d4d2,#929290,#4c4c4c)"></div>
  <div class="date">Mon 7 Jan 2017</div>
  <h3>Awesome consectetur adipiscing<br>Guidelines elit</h3>
  <a class="btn btn-green" style="left:45px">MORE</a><a class="btn btn-orange" style="left:172px">BOOK</a>
</article>
<article class="abs event-card" style="left:795px">
  <div class="photo" role="img" aria-label="Large crowd exercising on a field at an outdoor festival" style="background:radial-gradient(ellipse at 50% 55%,#6a5e5a 0,rgba(106,94,90,0) 35%),radial-gradient(ellipse at 70% 20%,#f1f3f3 0,rgba(241,243,243,0) 15%),linear-gradient(180deg,#d6e0e4 0%,#4f7a3c 24%,#6b7d55 45%,#4f6238 100%)"></div>
  <div class="date">Mon 7 Jan 2017</div>
  <h3>Awesome consectetur adipiscing<br>Guidelines elit</h3>
  <a class="btn btn-green" style="left:45px">MORE</a><a class="btn btn-orange" style="left:172px">BOOK</a>
</article>

<section class="abs news" role="img" aria-label="Blurred audience clapping at a presentation"></section>
<h2 class="abs news-title">LATEST FROM BRACKENMOOR</h2>
<article class="abs news-card" style="left:74px">
  <svg class="fold" width="44" height="44" viewBox="0 0 44 44"><path d="M0 0H44V44Z" fill="#8b8f94"/><path d="M0 0 44 44H0Z" fill="#d8d8d8"/></svg>
  <h4>Awesome consectetur adipis Guidelines elit</h4>
  <p>Ut enim ad minim veniam, quis nostrud Duis aute irure dolor in reprehenderit in voluptate velit esse cillum dolore eu fugiat nulla pariatur.</p>
  <a class="btn-outline">MORE</a>
</article>
<article class="abs news-card" style="left:434px">
  <svg class="fold" width="44" height="44" viewBox="0 0 44 44"><path d="M0 0H44V44Z" fill="#8b8f94"/><path d="M0 0 44 44H0Z" fill="#d8d8d8"/></svg>
  <h4>Awesome consectetur adipis Guidelines elit</h4>
  <p>Ut enim ad minim veniam, quis nostrud Duis aute irure dolor in reprehenderit in voluptate velit esse cillum dolore eu fugiat nulla pariatur.</p>
  <a class="btn-outline">MORE</a>
</article>
<article class="abs news-card" style="left:795px">
  <svg class="fold" width="44" height="44" viewBox="0 0 44 44"><path d="M0 0H44V44Z" fill="#8b8f94"/><path d="M0 0 44 44H0Z" fill="#d8d8d8"/></svg>
  <h4>Awesome consectetur adipis Guidelines elit</h4>
  <p>Ut enim ad minim veniam, quis nostrud Duis aute irure dolor in reprehenderit in voluptate velit esse cillum dolore eu fugiat nulla pariatur.</p>
  <a class="btn-outline">MORE</a>
</article>
<a class="abs see-all">SEE ALL NEWS</a>

<article class="abs tile tile-blue" style="left:74px">
  <div class="photo" role="img" aria-label="Speaker presenting to a conference audience" style="background:radial-gradient(ellipse at 25% 55%,#1e2430 0,rgba(30,36,48,0) 22%),radial-gradient(ellipse at 70% 70%,#d48a5a 0,rgba(212,138,90,0) 35%),radial-gradient(ellipse at 60% 15%,#e8a56a 0,rgba(232,165,106,0) 20%),linear-gradient(135deg,#6a2e1a,#b8603a,#4a2a20)"></div>
  <div class="band"></div>
  <div class="badge"><svg width="30" height="30" viewBox="0 0 30 30" fill="none" stroke="#fff" stroke-width="2"><circle cx="15" cy="11" r="5"/><path d="M6 26c1-6 5-9 9-9s8 3 9 9"/></svg></div>
  <h3>CONFERENCES &amp; EVENTS</h3>
  <a class="btn-line">MORE</a>
</article>
<article class="abs tile tile-green" style="left:434px">
  <div class="photo" role="img" aria-label="Friends laughing together at a party" style="background:radial-gradient(circle at 15% 15%,rgba(255,210,140,.6) 0,rgba(255,210,140,0) 10%),radial-gradient(circle at 80% 20%,rgba(255,200,120,.5) 0,rgba(255,200,120,0) 12%),radial-gradient(ellipse at 40% 60%,#9a6a48 0,rgba(154,106,72,0) 30%),radial-gradient(ellipse at 80% 70%,#2e4050 0,rgba(46,64,80,0) 28%),linear-gradient(135deg,#2c2620,#6a4c34,#2a2420)"></div>
  <div class="band"></div>
  <div class="badge"><svg width="30" height="30" viewBox="0 0 30 30" fill="none" stroke="#fff" stroke-width="2"><path d="M8 5h6l-1 8a2 2 0 0 1-4 0z"/><path d="M11 15v9M8 24h6"/><path d="M17 5h6l-1 8a2 2 0 0 1-4 0z"/><path d="M20 15v9M17 24h6"/></svg></div>
  <h3>PARTIES AT BRACKENMOOR</h3>
  <a class="btn-line">MORE</a>
</article>
<article class="abs tile tile-orange" style="left:795px">
  <div class="photo" role="img" aria-label="Hands typing on a laptop keyboard" style="background:radial-gradient(ellipse at 80% 20%,#fbf6ee 0,rgba(251,246,238,0) 30%),radial-gradient(ellipse at 45% 55%,#5c5854 0,rgba(92,88,84,0) 30%),radial-gradient(ellipse at 30% 25%,#c79a80 0,rgba(199,154,128,0) 18%),linear-gradient(135deg,#e8e2da,#b4a99e,#7f756c)"></div>
  <div class="band"></div>
  <div class="badge"><svg width="30" height="30" viewBox="0 0 30 30" fill="none" stroke="#fff" stroke-width="2"><rect x="4" y="6" width="16" height="11" rx="2"/><path d="M8 17v4l4-4"/><rect x="12" y="12" width="14" height="10" rx="2"/></svg></div>
  <h3>CO-WORKING HUB</h3>
  <a class="btn-line">MORE</a>
</article>

<section class="abs sports" role="img" aria-label="People working out on treadmills in a gym"></section>
<h2 class="abs sports-title">SPORTS &amp; LEISURE</h2>
<div class="abs sports-sub">CLICK FOR MORE INFORMATION</div>

<footer class="abs site-footer"></footer>
<div class="abs footer-col" style="left:74px">Brackenmoor Halls Entertainment Venue<br>Larkfield Close<br>Ashcombe<br>Dunmere<br>AC14 7RL</div>
<div class="abs footer-col" style="left:344px">What's On<br>Conferencing &amp; Events<br>Sports &amp; Leisure<br>Lantern Theatre</div>
<div class="abs footer-col" style="left:614px">Plan Your Visit<br>News<br>Discover More<br>Contact Us</div>
<div class="abs footer-brand">BRACKENMOOR<br>HALLS</div>
<div class="abs copyright">Copyright © 2016 brackenmoorhalls.co.uk All Rights Reserved</div>

</body>
</html>
```